VARNOLA SYSTEMS BUSINESS CARD DESIGN

WE WANT COMPLETE NEW DESIGN OF OUR BUSINESS CARD. WE ARE AN INTEGRATION COMPANY, WHERE WE INTEGRATE IOT/SMART SYSTEMS TO HOMES AND CORPORATE CUSTOMERS. WE SUPPLY AND INSTALL AUTOMATION PRODUCTS. THE FINAL DESIGN SHOULD COMMUNICATE TECHNOLOGY. THE CARD DESIGN SHOULD BE VERY IMPACT FULL. LOGO NEEDS TO BE THERE. IT WOULD NICE IF THE DESIGN WAS CLEAN. COLORS IS UP TO DESIGNER TO PLAY WITH, OR CAN STICK TO CORPORATE COLORS (FOLLOW LOGO). I HAVE ADDED FEW REFERENCE PHOTOS TO DRAW INSPIRATION MAYBE. I HAVE ADDED A HEX DESIGN, ITS NOT NECESSARY TO USE THIS DESIGN, ITS UPTO DESIGNER, JUST ADDED IF NEEDED TO PLAY WITH DESIGN.

Target Market(s)

Private end users and corporate clients

Industry/Entity Type

technology, home automation, home theaters, building management systems, IOT

Contact Information for Business Card

It should include Employee name, personal number, office number, email address, both in English and arabic. DETAILS TO INCLUDE :GERALD MOSSANE, MOBILE 0097150738915,OFFCIE 009714386207, GERALD@VARNOLAHUB.CO

Requirements
Must have
• Should feel like a technology company from design. Details both and in English and arabic (or at least have provision for arabic in design).
Nice to have
• I would like logo on one side, and details on the other side. Logo design side should communicate technology with logo. Other side can be clean just with information or also have some design aspects following from logo side. it would be interesting to see submissions with square design as well (that looks like an app Icon). colors could be of logo, red black grey and white. I have added some designs to draw inspiration from

```html
<!DOCTYPE html>
<html lang="en">
<head>
<meta charset="utf-8">
<title>Varnola Systems – Business Card</title>
<link rel="stylesheet" href="https://fonts.googleapis.com/css2?family=Montserrat:wght@400;500;700;800&display=swap">
<style>
  :root {
    --page: #e9e6e2;
    --card: #1b1a1b;
    --white: #ffffff;
    --grey: #a7a8ab;
    --red: #e3232a;
    --trace: #6c6c70;
  }
  * { box-sizing: border-box; margin: 0; padding: 0; }
  html, body { width: 1200px; height: 800px; overflow: hidden; }
  body {
    background: var(--page);
    font-family: "Montserrat", Arial, sans-serif;
    position: relative;
  }
  .card {
    position: absolute;
    top: 160px;
    width: 480px;
    height: 480px;
    border-radius: 42px;
    background: var(--card);
    overflow: hidden;
    box-shadow: 0 18px 40px rgba(0,0,0,.25);
  }
  .card--front { left: 90px; }
  .card--back { left: 630px; }

  /* front: circuit trace zones */
  .circuit-area { position: absolute; }
  .circuit-area--left {
    left: 0; top: 250px; width: 200px; height: 170px;
    background: linear-gradient(60deg, rgba(140,140,145,.45) 0%, rgba(108,108,112,.2) 55%, rgba(27,26,27,0) 90%);
    clip-path: polygon(0 10%, 70% 0, 100% 60%, 55% 100%, 0 100%);
  }
  .circuit-area--right {
    right: 0; top: 150px; width: 190px; height: 190px;
    background: linear-gradient(240deg, rgba(140,140,145,.45) 0%, rgba(108,108,112,.2) 55%, rgba(27,26,27,0) 90%);
    clip-path: polygon(30% 0, 100% 15%, 100% 100%, 20% 90%, 0 45%);
  }

  /* front: brand block */
  .brand {
    position: absolute;
    left: 0; right: 0; top: 200px;
    text-align: center;
  }
  .brand__line {
    display: inline-flex;
    align-items: center;
    gap: 12px;
    white-space: nowrap;
  }
  .brand__dot {
    width: 32px; height: 32px; border-radius: 50%;
    background: var(--red);
    flex: none;
  }
  .brand__name {
    color: var(--white);
    font-weight: 800;
    font-size: 30px;
    letter-spacing: 1px;
  }
  .brand__tagline {
    margin-top: 16px;
    color: var(--white);
    font-weight: 500;
    font-size: 12px;
    letter-spacing: 4px;
    white-space: nowrap;
  }

  /* back: triangle mosaic zone */
  .triangle-area {
    position: absolute;
    right: 0; top: 30px;
    width: 320px; height: 240px;
    background:
      linear-gradient(135deg, rgba(255,255,255,.9) 0%, rgba(167,168,171,.85) 35%, rgba(227,35,42,.9) 65%, rgba(167,168,171,.7) 85%, rgba(27,26,27,0) 100%);
    clip-path: polygon(45% 0, 60% 0, 60% 15%, 100% 15%, 100% 100%, 40% 100%, 40% 75%, 10% 75%, 10% 40%, 30% 40%, 30% 15%, 45% 15%);
  }

  /* back: details */
  .details {
    position: absolute;
    left: 40px; top: 285px;
    color: var(--white);
  }
  .details__name {
    font-weight: 800;
    font-size: 20px;
    letter-spacing: 1.5px;
    white-space: nowrap;
  }
  .details__role {
    color: var(--red);
    font-weight: 500;
    font-size: 17px;
    letter-spacing: 1.5px;
    margin-bottom: 16px;
  }
  .contact {
    list-style: none;
    font-size: 16px;
    line-height: 30px;
    letter-spacing: .5px;
  }
  .contact__item { display: flex; align-items: center; gap: 12px; white-space: nowrap; }
  .contact__icon { width: 20px; height: 20px; flex: none; }
</style>
</head>
<body>

<section class="card card--front" aria-label="Card front">
  <div class="circuit-area circuit-area--left" role="img" aria-label="Circuit board trace pattern"></div>
  <div class="circuit-area circuit-area--right" role="img" aria-label="Circuit board trace pattern"></div>
  <div class="brand">
    <div class="brand__line">
      <span class="brand__dot"></span>
      <span class="brand__name">VARNOLA SYSTEMS</span>
    </div>
    <p class="brand__tagline">A VARNOLA GROUP DIVISION.</p>
  </div>
</section>

<section class="card card--back" aria-label="Card back">
  <div class="triangle-area" role="img" aria-label="Mosaic of red, grey and white triangles"></div>
  <div class="details">
    <h1 class="details__name">GERALD MOSSANE</h1>
    <p class="details__role">DIRECTOR</p>
    <ul class="contact">
      <li class="contact__item">
        <svg class="contact__icon" viewBox="0 0 20 20" aria-hidden="true">
          <circle cx="10" cy="10" r="8.5" fill="none" stroke="#e3232a" stroke-width="1.5"/>
          <path d="M7 5.5l2 2-1 1.2c.6 1.4 1.6 2.4 3 3l1.2-1 2 2-1.3 1.5C9.8 13.8 6.2 10.2 5.8 7z" fill="#e3232a"/>
        </svg>
        <span>009 7150 7389 15</span>
      </li>
      <li class="contact__item">
        <svg class="contact__icon" viewBox="0 0 20 20" aria-hidden="true">
          <circle cx="10" cy="10" r="8.5" fill="none" stroke="#e3232a" stroke-width="1.5"/>
          <rect x="7" y="5" width="6" height="10" rx="1" fill="none" stroke="#e3232a" stroke-width="1.4"/>
        </svg>
        <span>009 7143 86207</span>
      </li>
      <li class="contact__item">
        <svg class="contact__icon" viewBox="0 0 20 20" aria-hidden="true">
          <circle cx="10" cy="10" r="8.5" fill="none" stroke="#e3232a" stroke-width="1.5"/>
          <rect x="5.5" y="7" width="9" height="6.5" fill="#e3232a"/>
          <path d="M5.5 7l4.5 3.5L14.5 7" fill="none" stroke="#1b1a1b" stroke-width="1"/>
        </svg>
        <span>Gerald@varnolahub.co</span>
      </li>
    </ul>
  </div>
</section>

</body>
</html>
```